Lumen Narration - Voiceover Services Product Flyer - Adobe Photoshop output required.

Simple PDF printable flyer (A4 sized high-resolution) (basic text provided in MS Publisher file attached) for our retained voice services.

Service being advertised:
From just $99/month for unlimited (per store) voice services.

Looking for a layered PSD (Adobe Photoshop) file allowing us to edit text as we refine it.

Need - Innovative graphics and layout.
Dynamic design.
--------------------------
BROCHURE TEXT!

Messaging on Hold
Your client’s time IS valuable. Why not use those moments where you can’t immediately service their needs to entertain and educate your audience? Lumen Narration can bring your clients a professionally written and acted message that enhances your brand, reduces caller stress and bolsters your marketing message. Put simply, happy clients mean client retention and sales.
In Store and Recorded Announcements
Keep your clients informed, comfortable and happy—whether they’re waiting for you or walking through your retail store. Whether it’s in-store radio, on-hold messages or emergency voice messaging for fire or medical systems, Lumen Narration can provide a complete range of professionally scripted audio directions to ensure satisfaction, professional imaging and compliance.
Phone Systems—Interactive Voice Response (IVR)
Your phone system is often your client’s gateway to your company—and your IVR, or interactive voice responses are the ‘first impression’ your clients receive when calling you. So why settle for second-best for your first impression? Lumen Narration will provide you with a professionally scripted first impression that enhances your image, builds confidence and quickly directs your clients to their correct destination.

-------------
BLOCK TEXT
Your client’s respond to all five senses.
You might have the visuals right but what do your clients think when they HEAR your business?
--------------
Why Lumen Narration for all your voiceover needs?
Technology Innovation
Lumen Narration is a leading technology innovator and can provide you support for all major phone and marketing systems—from the oldest to the newest. We also partner with phone system providers to help you modernise your voice technology.
Competitive
We can provide you with unlimited voice work for your store from just $2 per day. We can also provide voice delivery hardware and message on hold systems.
Expertise
Lumen Narration have been providing voice services to an international audience for more than a decade.
Professionalism
We aren’t happy unless you’re happy. If you don’t like a prompt, we’ll re-record it free! We even include free script review each month with our retained voice service.
Partnership
We’re not just another voiceover studio. We have professional marketing writers that partner with you to help you script every event, season and prompt. We deliver new content as your need it top ensure that your message is never stale.
-----------------------
CONTACT PANEL
Call 02 8139 4620 or 0438 27 61 90
to discuss your needs directly with a leading Sydney-based voiceover specialist.
------------------------
URL PANEL
We are Lumen Narration. The Sound of Tomorrow (TM)
www.lumennarrate.example.au
-------------------------

NOTE: CLIENT LOGOS PROVIDED IN ATTACHED LOGO FILE (MS Publisher format) Please include at least the top bunch of logos. Can be two sided A4 if you find that works creatively!

Target Market(s)

Small business and corporate.

Industry/Entity Type

Product

Font styles to use
Serif
Sans Serif

Requirements
Must have
• Dynamic design. Graphics that incorporate a retail feel. We're pitching to companies that have PHONE SYSTEMS in place... IN STORE AUDIO and RETAIL audio needs.
Nice to have
• A focus on the SENSES. ie. Sense of hearing. (We're highlighting that retail first impressions made on the PHONE are all about the AUDIO).
Should not have
• Cheesy microphones.

```html
<!DOCTYPE html>
<html lang="en">
<head>
<meta charset="utf-8">
<title>Lumen Narration – Voiceover Services Flyer</title>
<link rel="stylesheet" href="https://fonts.googleapis.com/css2?family=Signika:wght@400;600;700&family=Arimo:wght@400;700&display=swap">
<style>
  :root {
    --magenta: #c4147a;
    --magenta-dark: #9e0c60;
    --pink-soft: #f6cfe3;
    --pink-wash: #fbe6f0;
    --ink: #333333;
    --white: #ffffff;
  }
  * { margin: 0; padding: 0; box-sizing: border-box; }
  html, body { width: 849px; height: 1200px; overflow: hidden; background: var(--white); }
  .flyer {
    position: relative;
    width: 849px; height: 1200px;
    background: var(--white);
    font-family: "Arimo", Arial, sans-serif;
    color: var(--ink);
    overflow: hidden;
  }
  .top-wash {
    position: absolute; left: 0; top: 0; width: 849px; height: 420px;
    background: radial-gradient(ellipse at 15% 20%, var(--pink-soft) 0%, var(--pink-wash) 45%, rgba(255,255,255,0) 75%);
  }
  .hero-art {
    position: absolute; left: 0; top: 0; width: 420px; height: 380px;
    background: radial-gradient(circle at 40% 45%, #3a3a3a 0%, #1c1c1c 30%, rgba(240,200,222,0.6) 55%, rgba(255,255,255,0) 72%);
  }
  .headline {
    position: absolute; right: 40px; top: 128px; width: 470px;
    font-family: "Signika", sans-serif;
    color: var(--magenta);
    text-align: right;
    line-height: 1.12;
  }
  .headline .lead { font-size: 27px; font-weight: 400; }
  .headline .big { font-size: 40px; font-weight: 600; }
  .headline .question { font-size: 27px; font-weight: 400; margin-top: 4px; }
  .headline .hear { font-size: 40px; font-weight: 700; }
  .why-tab {
    position: absolute; left: 444px; top: 360px; width: 380px; height: 24px;
    background: var(--magenta); color: var(--white);
    border-radius: 6px 6px 0 0;
    font-family: "Signika", sans-serif; font-size: 14px; font-style: normal;
    line-height: 24px; text-align: center;
  }
  .column { position: absolute; top: 396px; font-size: 11.2px; line-height: 1.55; }
  .column-left { left: 28px; width: 385px; }
  .column-right { left: 444px; width: 380px; }
  .column h3 { font-size: 11.2px; font-weight: 700; color: var(--ink); margin-top: 4px; }
  .column-right h3 { text-transform: uppercase; }
  .column p { margin-bottom: 16px; }
  .footer-band {
    position: absolute; left: 0; top: 1046px; width: 849px; height: 72px;
    background: var(--pink-soft);
  }
  .url-panel {
    position: absolute; left: 0; top: 1046px; width: 430px; height: 72px;
    background: var(--magenta); color: var(--white);
    padding: 9px 0 0 40px;
  }
  .url-panel .tagline { font-size: 12px; }
  .url-panel .url { font-family: "Signika", sans-serif; font-size: 25px; font-weight: 600; line-height: 1.3; }
  .contact-panel {
    position: absolute; left: 452px; top: 1052px; width: 380px; height: 60px;
    background: var(--white); color: var(--magenta);
    text-align: center; padding-top: 7px;
  }
  .contact-panel .numbers { font-family: "Signika", sans-serif; font-size: 19px; }
  .contact-panel .note { font-size: 11px; line-height: 1.3; }
</style>
</head>
<body>
<div class="flyer">
  <div class="top-wash"></div>
  <div class="hero-art" role="img" aria-label="Illustration of a classic telephone with soft pink circles behind it"></div>

  <div class="headline">
    <div class="lead">Your client’s respond to all</div>
    <div class="big">five senses.</div>
    <div class="question">You might have the visuals right but what do your clients think when they</div>
    <div><span class="hear">HEAR</span> <span class="lead">your business?</span></div>
  </div>

  <div class="why-tab">Why Lumen Narration for all your voiceover needs?</div>

  <div class="column column-left">
    <h3>Messaging on Hold</h3>
    <p>Your client’s time IS valuable. Why not use those moments where you can’t immediately service their needs to entertain and educate your audience? Lumen Narration can bring your clients a professionally written and acted message that enhances your brand, reduces caller stress and bolsters your marketing message. Put simply, happy clients mean client retention and sales.</p>
    <h3>In Store and Recorded Announcements</h3>
    <p>Keep your clients informed, comfortable and happy—whether they’re waiting for you or walking through your retail store. Whether it’s in-store radio, on-hold messages or emergency voice messaging for fire or medical systems, Lumen Narration can provide a complete range of professionally scripted audio directions to ensure satisfaction, professional imaging and compliance.</p>
    <h3>Phone Systems—Interactive Voice Response (IVR)</h3>
    <p>Your phone system is often your client’s gateway to your company—and your IVR, or interactive voice responses are the ‘first impression’ your clients receive when calling you. So why settle for second-best for your first impression? Lumen Narration will provide you with a professionally scripted first impression that enhances your image, builds confidence and quickly directs your clients to their correct destination.</p>
  </div>

  <div class="column column-right">
    <h3>Technology Innovation</h3>
    <p>Lumen Narration is a leading technology innovator and can provide you support for all major phone and marketing systems—from the oldest to the newest. We also partner with phone system providers to help you modernise your voice technology.</p>
    <h3>Competitive</h3>
    <p>We can provide you with unlimited voice work for your store from just $2 per day. We can also provide voice delivery hardware and message on hold systems.</p>
    <h3>Expertise</h3>
    <p>Lumen Narration have been providing voice services to an international audience for more than a decade.</p>
    <h3>Professionalism</h3>
    <p>We aren’t happy unless you’re happy. If you don’t like a prompt, we’ll re-record it free! We even include free script review each month with our retained voice service.</p>
    <h3>Partnership</h3>
    <p>We’re not just another voiceover studio. We have professional marketing writers that partner with you to help you script every event, season and prompt. We deliver new content as your need it top ensure that your message is never stale.</p>
  </div>

  <div class="footer-band"></div>
  <div class="url-panel">
    <div class="tagline">We are Lumen Narration. The Sound of Tomorrow (TM)</div>
    <div class="url">www.lumennarrate.example.au</div>
  </div>
  <div class="contact-panel">
    <div class="numbers">Call 02 8139 4620 or 0438 27 61 90</div>
    <div class="note">to discuss your needs directly<br>with a leading Sydney-based voiceover specialist.</div>
  </div>
</div>
</body>
</html>
```